New Property management company business cards

Looking for a new business card, to reflect new younger ownership
Card should be clean, simple and professional but with a modern layout that is conveys our new logo and business model

Key aspects of the business:

Property Management
Facility Maintenance
Project Management
Tenant Improvements

Mailing Address:
PO BOX 7186
Modesto CA, 95353

Phone: 209-614-8837
Direct: 209-614-8831

Doyle Farrant
President

Target Market(s)

Commercial property owners

Industry/Entity Type

Real Estate property management

Contact Information for Business Card

Open to all designs but lean toward vertical layouts

Requirements
Must have
• Logo and space to customize name and contact info

```html
<!DOCTYPE html>
<html lang="en">
<head>
<meta charset="utf-8">
<title>Ardell Property Management – Business Card</title>
<link rel="stylesheet" href="https://fonts.googleapis.com/css2?family=Lato:wght@400;700&display=swap">
<style>
  :root {
    --ink: #353442;
    --slate: #363543;
    --slate-light: #4a4955;
    --teal: #1fb0a6;
    --paper: #ffffff;
    --mist: #e4efed;
    --grey: #d6d5d9;
  }
  * { box-sizing: border-box; margin: 0; padding: 0; }
  html, body {
    width: 1200px; height: 1000px; overflow: hidden;
    background: var(--paper);
    font-family: "Lato", Arial, sans-serif;
    color: var(--ink);
  }
  .canvas { position: relative; width: 1200px; height: 1000px; }

  /* Front */
  .card-front {
    position: absolute; left: 218px; top: 40px;
    width: 764px; height: 436px; background: var(--paper);
  }
  .front-accent {
    position: absolute; left: 464px; top: 17px;
    width: 300px; height: 393px;
    background: linear-gradient(90deg, var(--paper) 0%, var(--mist) 40%, var(--grey) 100%);
  }
  .brand {
    position: absolute; left: 40px; top: 60px; width: 302px;
    display: flex; flex-direction: column; align-items: center;
    font-weight: 700; color: var(--ink);
  }
  .brand-mark { width: 22px; height: 22px; background: var(--ink); margin-bottom: 14px; }
  .brand-name { font-size: 48px; letter-spacing: 6px; line-height: 1; text-transform: uppercase; }
  .brand-sub { font-size: 14px; letter-spacing: 4.6px; margin-top: 8px; text-transform: uppercase; white-space: nowrap; }

  .name-block { position: absolute; left: 0; top: 266px; height: 63px; }
  .name-bar {
    position: absolute; left: 0; top: 0; width: 29px; height: 63px;
    background: var(--slate);
  }
  .person-name {
    position: absolute; left: 40px; top: 6px; white-space: nowrap;
    font-size: 28px; font-weight: 700; color: #000;
  }
  .person-title {
    position: absolute; left: 41px; top: 40px; white-space: nowrap;
    font-size: 16px; color: #000;
  }
  .contact { position: absolute; left: 40px; top: 354px; font-size: 17px; color: #000; line-height: 22px; }
  .contact-line { display: flex; align-items: center; gap: 5px; white-space: nowrap; }
  .contact-line svg { width: 16px; height: 14px; }
  .address-band {
    position: absolute; left: 0; bottom: 0; width: 764px; height: 26px;
    background: var(--slate); color: #fff; font-size: 17px;
    text-align: center; line-height: 26px;
  }

  /* Back */
  .card-back {
    position: absolute; left: 218px; top: 507px;
    width: 764px; height: 436px; background: var(--slate); overflow: hidden;
  }
  .back-accent {
    position: absolute; left: 102px; top: 0; width: 580px; height: 436px;
    background: radial-gradient(ellipse at 50% 60%, var(--slate-light) 0%, var(--slate-light) 35%, var(--slate) 72%);
  }
  .card-back .brand {
    left: 182px; top: 118px; width: 400px; color: var(--paper);
  }
  .card-back .brand-mark { width: 30px; height: 30px; background: var(--paper); margin-bottom: 48px; }
  .card-back .brand-name { font-size: 58px; letter-spacing: 8px; }
  .card-back .brand-sub { font-size: 18px; letter-spacing: 5.4px; margin-top: 10px; }
</style>
</head>
<body>
<main class="canvas">
  <section class="card-front">
    <div class="front-accent" role="img" aria-label="Faint brand watermark area"></div>

    <div class="brand">
      <span class="brand-mark"></span>
      <span class="brand-name">Ardell</span>
      <span class="brand-sub">Property Management</span>
    </div>

    <div class="name-block">
      <span class="name-bar"></span>
      <h1 class="person-name">Doyle Farrant</h1>
      <p class="person-title">President</p>
    </div>

    <div class="contact">
      <p class="contact-line">
        <svg viewBox="0 0 16 14" aria-hidden="true"><path d="M1 4c0-2 3-3 7-3s7 1 7 3v1h-4V4H5v1H1z M3 6h10l2 7H1z" fill="#353442"/><circle cx="8" cy="9.5" r="2" fill="#fff"/></svg>
        209-614-8837
      </p>
      <p class="contact-line">
        <svg viewBox="0 0 16 14" aria-hidden="true"><path d="M1 4c0-2 3-3 7-3s7 1 7 3v1h-4V4H5v1H1z M3 6h10l2 7H1z" fill="#353442"/><circle cx="8" cy="9.5" r="2" fill="#fff"/></svg>
        209-614-8831 ( Direct )
      </p>
    </div>

    <div class="address-band">PO BOX 7186 Modesto CA, 95353</div>
  </section>

  <section class="card-back">
    <div class="back-accent" role="img" aria-label="Large faint brand watermark area"></div>
    <div class="brand">
      <span class="brand-mark"></span>
      <span class="brand-name">Ardell</span>
      <span class="brand-sub">Property Management</span>
    </div>
  </section>
</main>
</body>
</html>
```